Lake of the Ozarks Anniversary Flag

Looking for a flag design that incorporates the outline of the Lake of the Ozarks on a white background with some additional wording/ design incorporated. Would like the lake outline in Navy Blue. On the top of the flag "LAKE OF THE OZARKS" in all caps (possibly also in Navy Blue with a bright red outline. In the background, large and centered in subdued gray "90th." Bottom left corner "1931" and bottom right corner "2021." Possibly also add a compass somewhere (possibly in the void to the middle left area. This is a flag being designed for boats that is to commemorate the 90th anniversary of Lake of the Ozarks this year. I have a couple more lake outlines I have screenshotted but this website won't seem to download them. I can send them separate if that assists.

```html
<!DOCTYPE html>
<html lang="en">
<head>
<meta charset="utf-8">
<title>Lake of the Ozarks 90th Anniversary Flag</title>
<link href="https://fonts.googleapis.com/css2?family=Jost:wght@600;700&display=swap" rel="stylesheet">
<style>
  :root {
    --navy: #27276e;
    --signal-red: #e0202e;
    --subdued-gray: #666666;
    --flag-white: #ffffff;
    --backdrop: #d4d4d6;
  }
  * { margin: 0; padding: 0; box-sizing: border-box; }
  html, body {
    width: 1200px;
    height: 720px;
    overflow: hidden;
    background: var(--backdrop);
    font-family: "Jost", "Futura", sans-serif;
  }
  .flag {
    position: absolute;
    left: 20px;
    top: 74px;
    width: 1160px;
    height: 572px;
    background: var(--flag-white);
    overflow: hidden;
  }
  .flag-title {
    position: absolute;
    left: 0;
    top: 22px;
    width: 100%;
    font-weight: 700;
    font-size: 88px;
    line-height: 1;
    color: var(--navy);
    text-shadow:
      1px 0 0 var(--signal-red), -1px 0 0 var(--signal-red),
      0 1px 0 var(--signal-red), 0 -1px 0 var(--signal-red),
      1px 1px 0 var(--signal-red), -1px -1px 0 var(--signal-red),
      1px -1px 0 var(--signal-red), -1px 1px 0 var(--signal-red);
    white-space: nowrap;
    text-align: center;
    transform: scaleX(0.9);
    transform-origin: center;
  }
  .lake-outline {
    position: absolute;
    left: 494px;
    top: 114px;
    width: 582px;
    height: 427px;
  }
  .anniversary {
    position: absolute;
    left: 426px;
    top: 134px;
    font-weight: 700;
    font-size: 298px;
    line-height: 1;
    letter-spacing: -6px;
    color: var(--subdued-gray);
    white-space: nowrap;
    transform: scaleX(0.88);
    transform-origin: left top;
  }
  .anniversary-suffix {
    position: absolute;
    left: 745px;
    top: 171px;
    font-weight: 600;
    font-size: 58px;
    line-height: 1;
    color: var(--subdued-gray);
  }
  .compass {
    position: absolute;
    left: 63px;
    top: 190px;
    width: 192px;
    height: 192px;
  }
  .year {
    position: absolute;
    top: 472px;
    font-weight: 700;
    font-size: 88px;
    line-height: 1;
    color: var(--subdued-gray);
    white-space: nowrap;
  }
  .year-founded {
    left: 39px;
    transform: scaleX(0.83);
    transform-origin: left top;
  }
  .year-current {
    right: 40px;
    transform: scaleX(0.91);
    transform-origin: right top;
  }
</style>
</head>
<body>
  <main class="flag">
    <h1 class="flag-title">LAKE OF THE OZARKS</h1>

    <svg class="lake-outline" viewBox="0 0 582 427" role="img" aria-label="Navy blue outline map of the Lake of the Ozarks winding across the flag">
      <defs>
        <linearGradient id="lake-tone" x1="0" y1="0" x2="1" y2="1">
          <stop offset="0" stop-color="#27276e" stop-opacity="0.08"/>
          <stop offset="1" stop-color="#27276e" stop-opacity="0.22"/>
        </linearGradient>
      </defs>
      <rect x="0" y="0" width="582" height="427" fill="url(#lake-tone)"/>
    </svg>

    <div class="anniversary">90</div>
    <div class="anniversary-suffix">TH</div>

    <svg class="compass" viewBox="0 0 192 192" role="img" aria-label="Navy compass rose with north, south, east and west markings">
      <circle cx="96" cy="96" r="80" fill="var(--navy)" opacity="0.85"/>
    </svg>

    <div class="year year-founded">1931</div>
    <div class="year year-current">2021</div>
  </main>
</body>
</html>
```